Business Card & Email Signature Design || Upmarket + Luxury

Riverlume Honey, a New Zealand Manuka Honey company needs a Business Card & Email Signature design.

Our logo's are attached in Gold & Black versions, feel free to be creative with how you use the logo and it's patterns in your design.

Style:
- Looking for an Elegant, Luxurious, Upmarket feel.
- Black/Matte Black Card, Gold Foil, UV Embossing

Information to Add:

- Logo
- Company Name: Riverlume Honey
- Name: Mattias Brovell
- Title: Creative Director
- Phone: +64 2919 58 617
- Email: mattias@riverlumehoney.example
- Website: www.riverlumehoney.example

- Socials: ***For email Signature Only***
- Facebook: https://www.facebook.com/riverlumehoney/
- Instagram: https://www.instagram.com/riverlumehoney/

Target Market(s)

Asia/Europe Luxury, Upmarket

Contact Information for Business Card

- Logo
- Name: Mattias Brovell
- Phone: +64 2919 58 617

Font styles to use
Other font styles liked:
• Champagne & Limousines (Attached)

Requirements
Must have
• Business Card & Email Signature Design.

Looking for a Sleek, Luxury, Upmarket Design.

```html
<!DOCTYPE html>
<html lang="en">
<head>
<meta charset="utf-8">
<title>Riverlume Honey — Business Card</title>
<link href="https://fonts.googleapis.com/css2?family=Jost:wght@400;500;600&display=swap" rel="stylesheet">
<style>
  :root {
    --backdrop: #2b2b2d;
    --card: #0c0c0d;
    --card-edge: #1c1c1e;
    --gold: #d1a94e;
    --gold-soft: #a8843a;
    --silver: #c9c9cc;
    --ink-light: #ecebe7;
    --rule: #8a7546;
  }
  * { box-sizing: border-box; margin: 0; padding: 0; }
  html, body {
    width: 1200px; height: 900px; overflow: hidden;
    background: var(--backdrop);
    font-family: "Jost", "Century Gothic", sans-serif;
  }
  .sheet {
    width: 1200px; height: 900px;
    display: flex; flex-direction: column;
    align-items: center; justify-content: center; gap: 56px;
  }
  .card {
    position: relative;
    width: 660px; height: 377px;
    background: var(--card);
    border-radius: 22px;
    box-shadow: 0 0 0 1px var(--card-edge);
  }

  /* front */
  .card-front { display: flex; align-items: center; }
  .brand-seal {
    width: 330px; height: 100%;
    display: flex; align-items: center; justify-content: center;
  }
  .seal-ring {
    width: 200px; height: 200px; border-radius: 50%;
    display: flex; align-items: center; justify-content: center;
    border: 2px solid var(--gold);
  }
  .seal-name {
    width: 150px; text-align: center;
    font-size: 22px; font-weight: 500; letter-spacing: 3px;
    text-transform: uppercase; line-height: 1.3;
    color: var(--gold);
  }
  .divider {
    width: 1px; height: 190px;
    background: var(--rule);
  }
  .contact-block { padding-left: 34px; }
  .person-name {
    font-size: 31px; font-weight: 600; letter-spacing: 0.5px;
    text-transform: uppercase; color: var(--gold); line-height: 1;
  }
  .person-title {
    margin-top: 6px;
    font-size: 18px; font-weight: 400; color: var(--ink-light);
  }
  .contact-list { list-style: none; margin-top: 22px; }
  .contact-list li {
    display: flex; align-items: center; gap: 10px;
    font-size: 15.5px; color: var(--ink-light);
    line-height: 1; margin-bottom: 10px;
  }
  .contact-list li.web { color: var(--gold); }
  .contact-icon { width: 17px; height: 17px; flex: none; }

  /* back */
  .card-back { display: flex; align-items: center; justify-content: center; }
  .card-back .seal-ring { border-color: var(--silver); width: 210px; height: 210px; }
  .card-back .seal-name { color: var(--silver); }
</style>
</head>
<body>
<main class="sheet">

  <section class="card card-front" aria-label="Business card front">
    <div class="brand-seal">
      <div class="seal-ring"><span class="seal-name">Riverlume Honey</span></div>
    </div>
    <div class="divider"></div>
    <div class="contact-block">
      <h1 class="person-name">Mattias Brovell</h1>
      <p class="person-title">Creative Director</p>
      <ul class="contact-list">
        <li>
          <svg class="contact-icon" viewBox="0 0 24 24" fill="none" stroke="#d1a94e" stroke-width="2" stroke-linecap="round" stroke-linejoin="round"><path d="M5 3h4l2 5-2.5 1.5a11 11 0 0 0 6 6L16 13l5 2v4a2 2 0 0 1-2 2A16 16 0 0 1 3 5a2 2 0 0 1 2-2z"/></svg>
          +64 2919 58 617
        </li>
        <li>
          <svg class="contact-icon" viewBox="0 0 24 24" fill="none" stroke="#d1a94e" stroke-width="2" stroke-linejoin="round"><rect x="2.5" y="5" width="19" height="14" rx="1"/><path d="M2.5 6l9.5 7 9.5-7"/></svg>
          mattias@riverlumehoney.example
        </li>
        <li class="web">
          <svg class="contact-icon" viewBox="0 0 24 24" fill="none" stroke="#d1a94e" stroke-width="1.8"><circle cx="12" cy="12" r="9.5"/><ellipse cx="12" cy="12" rx="4.2" ry="9.5"/><path d="M2.5 12h19M4 7h16M4 17h16"/></svg>
          www.riverlumehoney.example
        </li>
      </ul>
    </div>
  </section>

  <section class="card card-back" aria-label="Business card back">
    <div class="seal-ring"><span class="seal-name">Riverlume Honey</span></div>
  </section>

</main>
</body>
</html>
```